Sports Graphic Templates for Action Photos

I am looking for a graphic design template for sports action photos. This needs to be simple enough that someone without expertise in Photoshop (use this program) can upload an image into a layer or what not and export the file for use.

The file needs to be 1280x720 and MUST incorporate the attached QUILLS graphic in some form or fashion. How is up to you.

Orbitron and DinPro are the two fonts I want to have used in the design. It can be one or it can be both.

Ideally - this template can be used for multiple graphics using similar action shots. Athlete of the Week or Athlete of the Year are two examples.

One other note - the QUILLS graphic needs to be incorporated somehow and it would be good to be able to interchange the coloring. The file uploaded is blue but we'd like to be able to match the colors to other photos or pull coloring from other parts of the image.

The image or action shot must not be cut out or altered other than to have certain styles applied. As mentioned above this would need to be updated by someone with limited Photoshop knowledge.

Examples:

http://www.hoopvarta.com/falconers/releases/player-of-the-week-doran-160404

https://tessmorathletics.com/news/2017/10/9/womens-soccer-lisa-varnet-adds-another-coral-ridge-player-of-the-week-award.aspx?path=wsoc

http://www.hoopvarta.com/tavin-week

https://k7pwm2zrfaqo58.imgvaultcdn.net/900x407_/media/14124/2560x1300-potywinner-belcastro.jpg

https://morvenhawks.com/images/2017/5/15/SB_Lakeshore_9_Awards_Social_Media_Graphic_Greta_Solvik_v1.jpg

https://thumbs-qx4.pictorelay.net/images?q=tbn:Vx82hTqLm04-77pR3KWdsZeBn91CfuAh56JoNwYtLqEaQ3XKrb9m

Target Market(s)

Action Shots Highlighting Achievement

Font styles to use
Other font styles liked:
• Orbitron and DinPro - one or both of those

Colors

Designer to choose colors to be used in the design.

Requirements
Must have
• Photoshop design. Use of the QUILLS graphis supplied - fonts (one or both) - 1280x720 sizing.
• Easy to use - someone with limited knowledge can easily update.
Nice to have
• Something that stands out from the rest. Examples were shown - none of those incorporate an action shot without the cutting out of the action or person in the image.
Should not have
• Any non-free textures or other items that need to be purchased.

```html
<!DOCTYPE html>
<html lang="en">
<head>
<meta charset="utf-8">
<title>Athlete of the Week – Template Set</title>
<link rel="stylesheet" href="https://fonts.googleapis.com/css2?family=Orbitron:wght@500;600&family=Barlow:wght@300&display=swap">
<style>
  :root {
    --page: #ffffff;
    --blue-deep: #0a1f6e;
    --blue-mid: #0d3fb8;
    --blue-night: #071447;
    --red-deep: #3a0608;
    --red-mid: #8c1016;
    --navy-night: #0a0b1c;
    --violet: #2b2a7a;
    --title-light: #ffffff;
    --title-shade: #a9adb8;
    --subtitle: #e8ecf5;
    --frame-line: rgba(255,255,255,.55);
    --frame-fill: rgba(255,255,255,.06);
  }
  * { box-sizing: border-box; margin: 0; padding: 0; }
  html, body {
    width: 1200px; height: 1200px; overflow: hidden;
    background: var(--page);
  }
  .template-set { position: relative; width: 1200px; height: 1200px; }
  .banner {
    position: absolute; left: 130px; width: 940px; height: 527px; overflow: hidden;
  }
  .banner--blue { top: 61px; }
  .banner--red { top: 612px; }

  .backdrop { position: absolute; inset: 0; }
  .banner--blue .backdrop {
    background:
      radial-gradient(ellipse 20% 20% at 88% 65%, rgba(70,190,210,.35), transparent 70%),
      linear-gradient(160deg, var(--blue-mid) 0%, var(--blue-deep) 55%, var(--blue-night) 100%);
  }
  .banner--red .backdrop {
    background:
      radial-gradient(ellipse 60% 14% at 40% 74%, rgba(180,40,80,.45), transparent 70%),
      linear-gradient(135deg, var(--navy-night) 0%, var(--red-deep) 45%, var(--red-mid) 100%);
  }
  .banner--red .backdrop::after {
    content: ""; position: absolute; inset: 0;
    background: linear-gradient(180deg, transparent 55%, rgba(43,42,122,.75) 100%);
  }

  /* action shot placeholder */
  .action-photo {
    position: absolute;
    border: 2px dashed var(--frame-line);
    background: var(--frame-fill);
  }
  .banner--blue .action-photo {
    left: 18px; top: 14px; width: 640px; height: 500px;
    background:
      radial-gradient(ellipse 45% 50% at 35% 45%, rgba(60,140,255,.45), transparent 75%),
      radial-gradient(ellipse 35% 45% at 78% 40%, rgba(40,110,230,.4), transparent 75%),
      var(--frame-fill);
  }
  .banner--red .action-photo {
    left: 300px; top: 14px; width: 380px; height: 500px;
    background:
      radial-gradient(ellipse 50% 50% at 55% 40%, rgba(200,30,40,.6), transparent 75%),
      var(--frame-fill);
  }
  .action-photo svg { position: absolute; inset: 0; width: 100%; height: 100%; }

  .light-streaks { position: absolute; inset: 0; width: 100%; height: 100%; }

  .title-lockup {
    position: absolute; left: 248px; top: 355px; width: 680px; text-align: left;
  }
  .title-main {
    display: block;
    font-family: "Orbitron", sans-serif; font-weight: 500;
    font-size: 80px; line-height: 1; letter-spacing: 30px;
    transform: skewX(-14deg);
    background: linear-gradient(180deg, var(--title-light) 35%, var(--title-shade) 100%);
    -webkit-background-clip: text; background-clip: text; color: transparent;
    filter: drop-shadow(2px 3px 4px rgba(0,0,0,.45));
  }
  .title-sub {
    display: block; margin-top: 6px; padding-left: 136px;
    font-family: "Barlow", sans-serif; font-weight: 300;
    font-size: 38px; line-height: 1; letter-spacing: 15px;
    color: var(--subtitle);
  }
</style>
</head>
<body>
<main class="template-set">

  <section class="banner banner--blue">
    <div class="backdrop"></div>
    <div class="action-photo" role="img" aria-label="Action photo: two wheelchair racers in helmets sprinting on a track, tinted blue">
      <svg viewBox="0 0 100 100" preserveAspectRatio="none" aria-hidden="true">
        <g stroke="rgba(255,255,255,.25)" stroke-width=".3" vector-effect="non-scaling-stroke" fill="none">
          <line x1="0" y1="0" x2="100" y2="100" vector-effect="non-scaling-stroke"/>
          <line x1="100" y1="0" x2="0" y2="100" vector-effect="non-scaling-stroke"/>
        </g>
      </svg>
    </div>
    <svg class="light-streaks" viewBox="0 0 940 527" aria-hidden="true">
      <g stroke="#9cc4ff" stroke-opacity=".28" stroke-width="2" fill="none">
        <line x1="0" y1="60" x2="420" y2="480"/>
        <line x1="0" y1="120" x2="380" y2="500"/>
        <line x1="0" y1="300" x2="230" y2="527"/>
        <line x1="380" y1="0" x2="940" y2="560"/>
        <line x1="560" y1="0" x2="940" y2="380"/>
        <line x1="640" y1="0" x2="940" y2="300"/>
        <line x1="700" y1="0" x2="940" y2="240"/>
      </g>
      <g fill="#4e8dff" fill-opacity=".12">
        <polygon points="420,0 520,0 940,420 940,520"/>
        <polygon points="0,200 0,260 260,527 200,527"/>
      </g>
    </svg>
    <div class="title-lockup">
      <span class="title-main">ATHLETE</span>
      <span class="title-sub">of the week</span>
    </div>
  </section>

  <section class="banner banner--red">
    <div class="backdrop"></div>
    <div class="action-photo" role="img" aria-label="Action photo: a football player in a red jersey carrying the ball, tinted red">
      <svg viewBox="0 0 100 100" preserveAspectRatio="none" aria-hidden="true">
        <g stroke="rgba(255,255,255,.25)" fill="none">
          <line x1="0" y1="0" x2="100" y2="100" vector-effect="non-scaling-stroke"/>
          <line x1="100" y1="0" x2="0" y2="100" vector-effect="non-scaling-stroke"/>
        </g>
      </svg>
    </div>
    <svg class="light-streaks" viewBox="0 0 940 527" aria-hidden="true">
      <g stroke="#ff6a70" stroke-opacity=".22" stroke-width="2" fill="none">
        <line x1="40" y1="40" x2="480" y2="480"/>
        <line x1="0" y1="220" x2="300" y2="527"/>
        <line x1="0" y1="280" x2="240" y2="527"/>
        <line x1="600" y1="0" x2="940" y2="340"/>
        <line x1="660" y1="0" x2="940" y2="280"/>
        <line x1="720" y1="0" x2="940" y2="220"/>
      </g>
      <g fill="#d4262f" fill-opacity=".14">
        <polygon points="80,0 160,0 560,400 480,400"/>
        <polygon points="0,300 0,360 160,527 100,527"/>
      </g>
    </svg>
    <div class="title-lockup">
      <span class="title-main">ATHLETE</span>
      <span class="title-sub">of the week</span>
    </div>
  </section>

</main>
</body>
</html>
```